Lotus Bridge Trust Flyer Design Project

We need an A5 one sided flyer design for a registered UK Charity Lotus Bridge Trust (Reg no 2263517). We support disadvantaged children in Goa, India. Our main project is Kestrel Lodge near Mapusa in North Goa. From their base at Kestrel Lodge they support around 150 children and provide uniforms and school bags to many more children. In addition to promoting this work we want to encourage people to visit them

You can read more about our work, logo and the colour scheme we use at www.lotusbridgetrust.org
We have a facebook page Lotus Bridge Trust

Our main project is Kestrel Lodge near Mapusa, Goa, India

Target Market(s)

simply those who might support our work

Industry/Entity Type

School

Requirements
Must have
• At least one photograph of children supported by Kestrel Lodge but these should be uplifting not showing children in distress. These must showcase our work i.e education, food and health

A photograph of Kestrel Lodge and its address and contact details. An invitation to visit Kestrel Lodge by contacting kestrelfund@quillpost.example or calling +917340528193

Our website, UK address facebook page and contact details. -info@lotusbridgetrust.org

It must be stated that we are a registered charity in England and Wales Reg. No 2263517

The following words must be included.
"We are a UK registered charity supporting disadvantaged children and young people in Goa, India regardless of their religion, class, caste or gender. The charity is administered entirely voluntarily which means that more of your money is available to fund our projects in Goa.

We aim to break the cycle of poverty and believe that education can transform lives.We focus on educational support but we know good health and nutrition are all essential to a child's chances of success at school and we therefore also provide meals and healthcare too.We support projects in Mapusa, Colva and Chimbel and we also fund a school uniform and school bag scheme which provides hundreds of uniforms and bags each year. Our main partner is The Kestrel Lodge Fund based at Kestrel Lodge near Mapusa.
You can read more about our work at www.lotusbridgetrust.org . However, if you are in Goa we welcome visits to Kestrel Lodge.
Nice to have
• A few inspiring photos of children

We would have liked to attach more but were limited to uploading 5
Should not have
• Photos of children in distress

```html
<!DOCTYPE html>
<html lang="en">
<head>
<meta charset="utf-8">
<title>Lotus Bridge Trust – Flyer</title>
<link rel="stylesheet" href="https://fonts.googleapis.com/css2?family=Noto+Sans:wght@400;700&family=Open+Sans:wght@700&family=Kaushan+Script&display=swap">
<style>
  :root {
    --bg: #fbf1d8;
    --paper: #ffffff;
    --brand-blue: #2f8ee6;
    --deep-blue: #1f5fa6;
    --sky: #cfe6f7;
    --sky-soft: #e8f3fb;
    --orange: #f08a1c;
    --ink: #1c1c1c;
    --white: #ffffff;
  }
  * { margin: 0; padding: 0; box-sizing: border-box; }
  html, body { width: 1200px; height: 848px; overflow: hidden; }
  body {
    background: var(--bg);
    font-family: "Noto Sans", Verdana, sans-serif;
    position: relative;
  }
  .flyer {
    position: absolute;
    left: 336px; top: 42px;
    width: 528px; height: 750px;
    background: var(--paper);
    overflow: hidden;
  }
  .flyer-art { position: absolute; inset: 0; }
  .brand {
    position: absolute; left: 18px; top: 16px;
    display: flex; align-items: center; gap: 14px;
  }
  .brand-mark {
    width: 84px; height: 84px; border-radius: 50%;
    background: var(--sky-soft);
    border: 3px solid var(--orange);
  }
  .brand-name {
    font-family: "Open Sans", Arial, sans-serif;
    font-weight: 700; font-size: 27px; line-height: 1;
    color: var(--brand-blue);
    margin-top: -30px;
  }
  .tagline {
    position: absolute; left: 118px; top: 54px;
    font-family: "Kaushan Script", cursive;
    font-size: 17px; color: var(--orange);
  }
  .intro {
    position: absolute; left: 31px; top: 141px; width: 336px;
    font-size: 13.3px; line-height: 15.9px; color: var(--ink);
    text-align: justify;
  }
  .intro p { text-indent: 24px; }
  .intro p.partner { text-indent: 14px; }
  .intro .highlight { color: var(--brand-blue); font-weight: 700; }
  .photo {
    position: absolute; border-radius: 10px;
  }
  .photo-child-chalk { left: 399px; top: 62px; width: 123px; height: 174px;
    background: linear-gradient(160deg, #b7764a, #7a4a2c); }
  .photo-children-colour { left: 399px; top: 248px; width: 123px; height: 175px;
    background: linear-gradient(160deg, #5b8fc8, #8a3e7a 60%, #3a3352); }
  .photo-child-meal { left: 399px; top: 435px; width: 123px; height: 173px;
    background: linear-gradient(160deg, #a77a55, #6d8bb0 60%, #c9b48d); }
  .photo-lodge { left: 30px; top: 477px; width: 174px; height: 99px;
    background: linear-gradient(180deg, #a9c9e6, #3f78b8 55%, #4f7a3a); }
  .photo-slates { left: 213px; top: 477px; width: 172px; height: 99px;
    background: linear-gradient(160deg, #a87a4a, #c85c4a 55%, #3c3a36); }
  .contact {
    position: absolute;
    font-family: "Noto Sans", Verdana, sans-serif;
    font-style: normal;
    font-weight: 700; font-size: 11px; line-height: 13.4px;
    color: var(--white);
    white-space: nowrap;
  }
  .contact-uk { left: 19px; top: 633px; }
  .contact-uk .org { font-size: 12.5px; }
  .contact-goa { right: 13px; top: 646px; text-align: right; }
  .footer-brand {
    position: absolute; left: 184px; top: 640px; width: 100px;
    display: flex; flex-direction: column; align-items: center; gap: 6px;
  }
  .footer-mark {
    width: 58px; height: 58px; border-radius: 50%;
    background: var(--sky-soft);
  }
  .footer-name {
    font-family: "Noto Sans", Verdana, sans-serif;
    font-weight: 700; font-size: 10px; color: var(--white);
    text-align: center; line-height: 1.2;
  }
</style>
</head>
<body>
  <main class="flyer">
    <svg class="flyer-art" width="528" height="750" viewBox="0 0 528 750" aria-hidden="true">
      <defs>
        <linearGradient id="header-wash" x1="0" y1="0" x2="0" y2="1">
          <stop offset="0" stop-color="#ffffff"/>
          <stop offset="1" stop-color="#d7ebf8"/>
        </linearGradient>
        <linearGradient id="footer-band" x1="0" y1="0" x2="0" y2="1">
          <stop offset="0" stop-color="#4aa3dc"/>
          <stop offset="1" stop-color="#1d5a9e"/>
        </linearGradient>
        <linearGradient id="side-band" x1="0" y1="0" x2="1" y2="0">
          <stop offset="0" stop-color="#bfe0f4"/>
          <stop offset="1" stop-color="#e4f2fb"/>
        </linearGradient>
      </defs>
      <rect x="0" y="90" width="528" height="560" fill="url(#header-wash)" opacity="0.45"/>
      <rect x="392" y="50" width="136" height="590" fill="url(#side-band)"/>
      <path d="M0 100 C 120 150, 300 120, 528 48 L528 62 C 300 132, 120 162, 0 118 Z" fill="#cfe6f7"/>
      <path d="M0 108 C 130 148, 310 108, 528 52 L528 58 C 310 116, 130 156, 0 114 Z" fill="var(--orange)"/>
      <path d="M0 118 C 140 150, 320 112, 528 60 L528 66 C 320 120, 140 158, 0 124 Z" fill="var(--brand-blue)"/>
      <path d="M0 600 C 140 575, 300 600, 528 628 L528 750 L0 750 Z" fill="url(#footer-band)"/>
      <path d="M0 596 C 140 570, 300 594, 528 620 L528 626 C 300 600, 140 578, 0 604 Z" fill="var(--orange)"/>
      <path d="M0 608 C 150 584, 310 606, 528 634 L528 640 C 310 614, 150 592, 0 616 Z" fill="#9fd0ef" opacity="0.7"/>
    </svg>

    <header class="brand">
      <span class="brand-mark"></span>
      <span class="brand-name">Lotus Bridge Trust</span>
    </header>
    <p class="tagline">Towards a brighter future</p>

    <section class="intro">
      <p>We are a UK registered charity supporting disadvantaged children and young people in Goa, India regardless of their religion, class, caste or gender. The charity is administered entirely voluntarily which means that more of your money is available to fund our projects in Goa.</p>
      <p>We aim to break the cycle of poverty and believe that education can transform lives. We focus on educational support but we know good health and nutrition are all essential to a child's chances of success at school and we therefore also provide meals and healthcare too.We support projects in Mapusa, Colva and Chimbel and we also fund a school uniform and school bag scheme which provides hundreds of uniforms and bags each year.</p>
      <p class="partner">Our main partner is The Kestrel Lodge Fund based at Kestrel Lodge near Mapusa. You can read more about our work at www.lotusbridgetrust.org However, if you are in Goa we welcome visits to <span class="highlight">Kestrel Lodge</span>.</p>
    </section>

    <div class="photo photo-lodge" role="img" aria-label="Photograph of Kestrel Lodge, a blue and white house with garden"></div>
    <div class="photo photo-slates" role="img" aria-label="Photograph of two smiling girls holding their school slates"></div>
    <div class="photo photo-child-chalk" role="img" aria-label="Photograph of a smiling boy holding a box of coloured chalk"></div>
    <div class="photo photo-children-colour" role="img" aria-label="Photograph of cheerful children covered in festival colours"></div>
    <div class="photo photo-child-meal" role="img" aria-label="Photograph of a boy enjoying a meal from a lunch box"></div>

    <address class="contact contact-uk">
      <span class="org">Lotus Bridge Trust,</span><br>
      Reg. No 2263517<br>
      The Willows,<br>
      Elmfield Road, Hallbrook<br>
      NORTHBY, S99 4QX<br>
      England<br>
      info@lotusbridgetrust.org<br>
      www.lotusbridgetrust.org
    </address>

    <div class="footer-brand">
      <span class="footer-mark"></span>
      <span class="footer-name">Lotus Bridge Trust</span>
    </div>

    <address class="contact contact-goa">
      The Kestrel Lodge Fund, Kestrel Lodge,<br>
      House Number 27/5,<br>
      Near Sunrise Clinic,<br>
      Ravanwada, Mapusa,<br>
      Bardez, Goa - 403511 INDIA<br>
      Tel : +917340528193<br>
      kestrelfund@quillpost.example
    </address>
  </main>
</body>
</html>
```